Chiropractic Condition Certificates

Hi,
I'd like have these certificates changed into jpegs with more modern colors and graphics. They need to be eye-catching with good looking images so they will work on Facebook. They need to be suitable to attach in a Facebook post. The current layout might not work for FB post. They may need to be more square then rectangular. Right now they are set up three to a page because In the past they were printed out and handed to patients. I don't need the new ones three to a page. I see these as being used as a jpeg photo in a FB post. Please remove the lines that say "*A $79.00 Value" and the line "MERIDIAN SPINE RELIEF AND RECOVERY CENTER. 72 HALVERY RD. DANBURY, CT 06810 555-318-2964", as they need to be suitable for use by many different chiropractors and not just one.

```html
<!DOCTYPE html>
<html lang="en">
<head>
<meta charset="utf-8">
<title>Chiropractic TMJ Referral Certificates</title>
<link rel="stylesheet" href="https://fonts.googleapis.com/css2?family=Jost:wght@400;500&family=Roboto+Condensed:wght@400;700&display=swap">
<style>
  :root {
    --page-bg: #ffffff;
    --card-light: #f3f8dc;
    --card-mid: #dbe9b4;
    --card-edge: #c4d99a;
    --brand-blue: #1a2fa0;
    --band-blue: #13249a;
    --band-dark: #0b1a7a;
    --title-blue: #1b34b4;
    --body-ink: #3a3a3a;
    --strong-ink: #333333;
    --white: #ffffff;
    --photo-skin: #d9b8a6;
    --photo-hair: #5a4034;
  }
  * { box-sizing: border-box; margin: 0; padding: 0; }
  html, body { width: 1200px; height: 593px; overflow: hidden; background: var(--page-bg); }
  .canvas { position: relative; width: 1200px; height: 593px; }

  .certificate {
    position: absolute; top: 2px; width: 590px; height: 589px;
    background: radial-gradient(ellipse at 55% 45%, var(--card-light) 0%, var(--card-mid) 70%, var(--card-edge) 100%);
    border: 1px solid #b9c99a;
    overflow: hidden;
    font-family: "Roboto Condensed", "Arial Narrow", sans-serif;
    color: var(--body-ink);
  }
  .certificate--gift { left: 3px; }
  .certificate--share { left: 607px; }

  .headline {
    position: absolute; left: 180px; top: 12px;
    font-family: "Jost", "Futura", sans-serif; font-weight: 400;
    font-size: 38px; line-height: 1; color: var(--title-blue); letter-spacing: 0.5px;
  }
  .band {
    position: absolute; left: 0; right: 0; top: 55px; height: 86px;
    background: linear-gradient(90deg, var(--band-dark) 0%, var(--band-blue) 40%, #2a3fb6 100%);
    border-top: 2px solid #0a1566;
  }
  .band__text {
    position: absolute; left: 180px; top: 11px; right: 4px;
    font-family: "Jost", "Futura", sans-serif; font-weight: 400;
    font-size: 25px; line-height: 36px; color: var(--white); letter-spacing: 0.2px;
  }
  .band__text .small { font-size: 21px; }
  .band__text .big { font-size: 28px; }

  .portrait {
    position: absolute; left: 16px; top: 31px; width: 158px; height: 152px;
    background: var(--white); padding: 6px;
    box-shadow: 1px 2px 4px rgba(0,0,0,0.45);
    border: 1px solid #777;
  }
  .portrait__fill {
    width: 100%; height: 100%;
    background: linear-gradient(160deg, #f2efec 0%, #e8dcd4 45%, var(--photo-skin) 75%, var(--photo-hair) 100%);
  }

  .intro {
    position: absolute; left: 182px; top: 150px; right: 18px;
    font-weight: 700; font-size: 14.5px; line-height: 18px; color: var(--strong-ink);
  }

  .body {
    position: absolute; left: 20px; right: 20px; top: 203px;
    text-align: justify; font-size: 14.6px; line-height: 19.5px; letter-spacing: -0.25px;
  }
  .body p + p { margin-top: 11px; }
  .certificate--share .body { left: 22px; right: 20px; font-size: 16.6px; line-height: 22.5px; letter-spacing: -0.1px; }
  .certificate--share .body p + p { margin-top: 12px; }

  .share-line {
    position: absolute; left: 0; right: 0; top: 430px; text-align: center;
    font-weight: 700; font-size: 15px; color: var(--brand-blue);
  }
  .offer {
    position: absolute; left: 18px; right: 18px; top: 458px; height: 72px;
    background: var(--band-blue); padding: 4px;
  }
  .offer__inner {
    width: 100%; height: 100%; border: 2px solid var(--white);
    display: flex; align-items: center; justify-content: center; text-align: center;
    color: var(--white); font-weight: 700; font-size: 15.5px; line-height: 22px; letter-spacing: 0.2px;
  }
  .fine-print {
    position: absolute; left: 24px; right: 20px; top: 537px;
    font-size: 10.6px; line-height: 14px; text-align: justify;
  }

  .share-box {
    position: absolute; left: 20px; right: 20px; top: 483px; height: 88px;
    background: var(--band-blue); padding: 5px;
  }
  .share-box__inner {
    width: 100%; height: 100%; border: 2px solid var(--white);
    display: flex; align-items: center; justify-content: center; text-align: center;
    color: var(--white); font-weight: 700; font-size: 23px; line-height: 30px;
  }
</style>
</head>
<body>
<main class="canvas">

  <section class="certificate certificate--gift">
    <div class="band">
      <div class="band__text">WHO HAS TEMPEROMANDIBULAR<br>JOINT <span class="big">(TMJ)</span> <span class="small">TODAY!</span></div>
    </div>
    <h1 class="headline">HELP SOMEONE</h1>
    <div class="portrait"><div class="portrait__fill" role="img" aria-label="Photo of a woman holding her jaw in pain"></div></div>
    <p class="intro">Your jaw joint or temperomandibular jont (TMJ) gets its name from the two bones which form the joint.</p>
    <div class="body">
      <p>The temporal bone of your skull and the mandible or jaw bone fit together to form a hinge-like joint. TMJ can cause headaches, ringing in your ear, face pain and pain across your neck and shoulders. Popping and clicking of the TMJ while opening your mouth or chewing indicates that your TMJ is not functioning properly. When an imbalance of the TMJ is found it can be corrected by balancing the jaw’s muscular activity with Chiropractic.</p>
      <p>Our mission in Chiropractic is to help people who are tired of just covering up their pain by taking drugs. We can't reach everyone personally to tell them that Chiropractic may be the answer to their problem. Let's both offer a helping hand. Refer those you know who could benefit from our care and we will offer honest and sincere assistance.</p>
    </div>
    <p class="share-line">Share this certificate to someone who we can help together with Chiropractic.</p>
    <div class="offer"><div class="offer__inner">THIS GIFT CERTIFICATE IS VALID FOR 2 WEEKS AND ENTITLES THE<br>BEARER TO A CONSULTATION &amp; EXAMINATION AT NO CHARGE.</div></div>
    <p class="fine-print">The recipient of this Gift Certificate will have NO charge for the first visit services described above. Should treatment be deemed necessary, the usual fees will be explained in advance. This certificate is not valid with Worker’s Comp and Personal Injury cases which often cover 100% of services.</p>
  </section>

  <section class="certificate certificate--share">
    <div class="band">
      <div class="band__text">WHO HAS TEMPEROMANDIBULAR<br>JOINT <span class="big">(TMJ)</span> <span class="small">TODAY!</span></div>
    </div>
    <h1 class="headline">HELP SOMEONE</h1>
    <div class="portrait"><div class="portrait__fill" role="img" aria-label="Photo of a woman holding her jaw in pain"></div></div>
    <p class="intro">Your jaw joint or temperomandibular jont (TMJ) gets its name from the two bones which form the joint.</p>
    <div class="body">
      <p>The temporal bone of your skull and the mandible or jaw bone fit together to form a hinge-like joint. TMJ can cause headaches, ringing in your ear, face pain and pain across your neck and shoulders. Popping and clicking of the TMJ while opening your mouth or chewing indicates that your TMJ is not functioning properly. When an imbalance of the TMJ is found it can be corrected by balancing the jaw’s muscular activity with Chiropractic.</p>
      <p>Our mission in Chiropractic is to help people who are tired of just covering up their pain by taking drugs. We can't reach everyone personally to tell them that Chiropractic may be the answer to their problem. Let's both offer a helping hand. Refer those you know who could benefit from our care and we will offer honest and sincere assistance.</p>
    </div>
    <div class="share-box"><div class="share-box__inner">Share this message with someone<br>who we can help together with Chiropractic.</div></div>
  </section>

</main>
</body>
</html>
```